Website For Custom Home Builder

-Very elegant and simple design as I am a high end custom home builder.
-I build homes $2 million to $10 million range so the website needs to reflect the level of home that I build.
-Attached are photos of homes I have built to use as well as my logo.
-I need final design to be in layered format so my local guy can edit if he needs to.

3 Page Design
1. HomePage:
-logo, some photos,
-“Building beautiful custom homes in Indianapolis for over 20 years”
2. AboutPage:
-Wade Holloran has been building stunning custom homes in the Indianpolis area for over 20 years. As a small boutique building company we only build a handful of homes a year in order to offer our clients the personal attention that their homes deserve. It's this attention to detail that makes our client experience and final product something special and unique.
- family photo
3. ContactPage:
-office photo
-317-552-7190
-wade@whcrafted.com
-415 North Fernmill Rd, Suite 308, Carmel IN 46033

Target Market(s)

Very high end clients looking to build $2 million to $10 million homes.

Industry/Entity Type

Residential high end custom home builder/construction

Coding

Coded - Design and coding required

Number of Pages Required

3 page

Requirements
Must have
• Very simple and elegant design that represents the high end homes that I build.
Nice to have
Should not have
• Should NOT have a lot of clutter or be a very busy page from a design perspective.

```html
<!DOCTYPE html>
<html lang="en">
<head>
<meta charset="utf-8">
<title>Contact Us – Wade Holloran Custom Homes</title>
<link href="https://fonts.googleapis.com/css2?family=Outfit:wght@300;400;500;600;700&display=swap" rel="stylesheet">
<style>
:root{
  --rust:#a6561a;
  --ink:#222222;
  --text:#3a3a3a;
  --muted:#6b6b6b;
  --blush:#f6ebe5;
  --paper:#f8f8f8;
  --line:#cfcfcf;
  --white:#ffffff;
}
*{box-sizing:border-box;margin:0;padding:0}
html,body{width:1019px;height:1200px;overflow:hidden;background:var(--white)}
body{position:relative;font-family:"Outfit",sans-serif;color:var(--text)}
.abs{position:absolute}

/* header */
.site-header{left:0;top:0;width:1019px;height:88px;background:var(--white)}
.brand{left:102px;top:26px;display:flex;align-items:center;gap:8px}
.brand-mark{width:14px;height:14px;background:var(--rust)}
.brand-name{font-size:17px;font-weight:500;color:var(--ink);line-height:1.1;letter-spacing:.3px}
.brand-name span{display:block;font-size:8.5px;letter-spacing:3.6px;text-transform:uppercase}
.main-nav{top:36px;font-size:10.5px;letter-spacing:.5px;text-transform:uppercase;color:var(--ink)}
.main-nav.active{color:var(--rust)}
.call-box{left:727px;top:0;width:292px;height:88px;background:var(--rust);color:var(--white);padding:22px 0 0 26px}
.call-label{font-size:15px;font-weight:300;letter-spacing:.6px;display:flex;align-items:center;gap:10px}
.call-number{font-size:23px;font-weight:600;letter-spacing:1px;margin-top:3px}

/* hero */
.hero{left:0;top:88px;width:1019px;height:255px;background:linear-gradient(120deg,#2b2a28 0%,#4b3e30 35%,#5e4a36 55%,#6f665c 80%,#8a7f73 100%)}
.hero-title{left:0;top:188px;width:1019px;text-align:center;color:var(--white);font-size:36px;font-weight:600;letter-spacing:.5px}
.divider{display:flex;gap:7px;align-items:center;justify-content:center}
.divider i{display:block;height:2px;background:currentColor}
.divider .long{width:38px}.divider .dot{width:4px}

/* contact card */
.contact-card{left:102px;top:406px;width:815px;height:286px}
.contact-info{left:0;top:0;width:416px;height:286px;background:var(--blush)}
.map-area{left:416px;top:0;width:399px;height:286px;background:linear-gradient(135deg,#ececec,#e2e2e2)}
.card-title{left:38px;top:36px;font-size:22px;font-weight:600;color:var(--ink)}
.card-divider{left:38px;top:66px;color:var(--ink)}
.info-icon{left:38px;width:38px;height:38px;border:1px solid var(--rust);border-radius:2px;display:flex;align-items:center;justify-content:center}
.info-link{left:62px;width:1px;height:7px;background:var(--rust);opacity:.5}
.info-text{left:95px;font-size:18.5px;font-weight:300;color:var(--text);line-height:22px;letter-spacing:.5px}
.info-text a{color:var(--rust);text-decoration:underline;text-underline-offset:3px}

/* enquiry */
.enquiry{left:0;top:755px;width:1019px;height:408px;background:var(--paper)}
.eyebrow{left:0;top:62px;width:1019px;text-align:center;color:var(--rust);font-size:16px;font-weight:300;letter-spacing:.5px}
.section-title{left:0;top:82px;width:1019px;text-align:center;font-size:35px;font-weight:600;color:var(--ink)}
.field{width:303px;height:32px;border:1px solid var(--line);background:var(--paper);font-size:10.5px;color:var(--muted);padding:9px 11px;letter-spacing:.3px}
.field.message{width:625px;height:64px}
.submit{left:459px;top:313px;width:102px;height:32px;border:1px solid var(--rust);color:var(--rust);font-size:10.5px;letter-spacing:.6px;display:flex;align-items:center;justify-content:center}

/* footer */
.site-footer{left:0;top:1163px;width:1019px;height:37px;background:var(--rust);color:var(--white);font-size:9px;font-weight:300;letter-spacing:.2px}
.site-footer b{font-weight:600}
.site-footer a{color:var(--white)}
.foot-item{top:14px}
</style>
</head>
<body>

<header class="site-header abs">
  <div class="brand abs">
    <span class="brand-mark"></span>
    <div class="brand-name">WADE HOLLORAN<span>Custom Homes</span></div>
  </div>
  <nav>
    <span class="main-nav abs" style="left:429px">Home</span>
    <span class="main-nav abs" style="left:508px">About Us</span>
    <span class="main-nav active abs" style="left:609px">Contact Us</span>
  </nav>
  <div class="call-box abs">
    <div class="call-label">CALL US
      <svg width="16" height="16" viewBox="0 0 24 24" fill="none" stroke="#fff" stroke-width="2"><path d="M5 3h4l2 5-3 2a12 12 0 0 0 6 6l2-3 5 2v4a2 2 0 0 1-2 2A18 18 0 0 1 3 5a2 2 0 0 1 2-2z"/></svg>
    </div>
    <div class="call-number">317-552-7190</div>
  </div>
</header>

<section class="hero abs" role="img" aria-label="Office interior photo with a live-edge wooden desk and leather chair"></section>
<h1 class="hero-title abs">CONTACT US</h1>
<div class="divider abs" style="left:0;top:234px;width:1019px;color:#fff"><i class="long"></i><i class="dot"></i><i class="long"></i></div>

<section class="contact-card abs">
  <div class="contact-info abs">
    <h2 class="card-title abs">CONTACT INFO</h2>
    <div class="card-divider divider abs"><i class="long"></i><i class="dot"></i><i class="long"></i></div>

    <div class="info-icon abs" style="top:93px">
      <svg width="16" height="16" viewBox="0 0 24 24" fill="none" stroke="#a6561a" stroke-width="1.5"><path d="M5 3h4l2 5-3 2a12 12 0 0 0 6 6l2-3 5 2v4a2 2 0 0 1-2 2A18 18 0 0 1 3 5a2 2 0 0 1 2-2z"/></svg>
    </div>
    <div class="info-text abs" style="top:101px">317-552-7190</div>
    <div class="info-link abs" style="top:138px"></div>

    <div class="info-icon abs" style="top:151px">
      <svg width="16" height="16" viewBox="0 0 24 24" fill="none" stroke="#a6561a" stroke-width="1.5"><path d="M3 10l9-6 9 6v10H3z"/><path d="M3 10l9 6 9-6"/></svg>
    </div>
    <div class="info-text abs" style="top:158px"><a>wade@whcrafted.com</a></div>
    <div class="info-link abs" style="top:195px"></div>

    <div class="info-icon abs" style="top:208px">
      <svg width="16" height="16" viewBox="0 0 24 24" fill="none" stroke="#a6561a" stroke-width="1.5"><path d="M3 6l6-2 6 2 6-2v14l-6 2-6-2-6 2z"/><circle cx="15" cy="9" r="2"/></svg>
    </div>
    <div class="info-text abs" style="top:206px">415 North Fernmill Rd,<br>Suite 308, Carmel IN 46033</div>
  </div>
  <div class="map-area abs" role="img" aria-label="Street map showing the office location"></div>
</section>

<section class="enquiry abs">
  <p class="eyebrow abs">ENQUIRY NOW!</p>
  <h2 class="section-title abs">CONTACT US</h2>
  <div class="field abs" style="left:197px;top:141px">Full Name</div>
  <div class="field abs" style="left:519px;top:141px">Email Address*</div>
  <div class="field abs" style="left:197px;top:185px">Phone Number*</div>
  <div class="field abs" style="left:519px;top:185px">Subject</div>
  <div class="field message abs" style="left:197px;top:230px">Messages...</div>
  <div class="submit abs">SUBMIT</div>
</section>

<footer class="site-footer abs">
  <span class="foot-item abs" style="left:102px"><b>E.:</b> <a>wade@whcrafted.com</a></span>
  <span class="foot-item abs" style="left:370px"><b>ADDRESS:</b> 415 North Fernmill Rd, Suite 308, Carmel IN 46033</span>
  <span class="foot-item abs" style="left:718px">© Copyright <a>Wade Holloran.</a> All Right Reserved.</span>
</footer>

</body>
</html>
```